Business Cards for a Junk Removal Company

Hello,
We are looking to have business cards designed that are simple, bold, easy to read, and right to the point. Please see the attachments for our logo files. We want the card to be yellow on both sides ( Color code Yellow: #FFE01B). The logo text font is (Rockstar Extra Bold) and this is also in the files attached. Please make the text black for the logo. On the back side of the card, you can use white and black for text. Thank you in advance for your hard work!

Front of card-
Harbor Haul Away (logo)
Back of card-
Harbor Haul Away
Donate - Recycle - Dispose
555-271-8093
www.harborhaulaway.example
info@harborhaulaway.example

Industry/Entity Type

Junk removal

Contact Information for Business Card

FRONT OF CARD- Harbor Haul Away (logo) BACK OF CARD- Harbor Haul Away Donate - Recycle - Dispose 555-271-8093 www.harborhaulaway.example info@harborhaulaway.example

Font styles to use
Other font styles liked:
• Rockstar Extra Bold

Colors
FFF300
FFF600
FEFA6F
FFFEC7
FFFEE8

Requirements
Must have
• Must have color code Yellow: #FFE01B for the background of front and back of the card

```html
<!DOCTYPE html>
<html lang="en">
<head>
<meta charset="utf-8">
<title>Harbor Haul Away – Business Cards</title>
<link rel="stylesheet" href="https://fonts.googleapis.com/css2?family=Anton&family=Poppins:wght@500;700&display=swap">
<style>
  :root {
    --yellow: #FFE01B;
    --black: #0B0B0B;
    --white: #FFFFFF;
    --backdrop: #CBCBCB;
  }
  * { margin: 0; padding: 0; box-sizing: border-box; }
  html, body { width: 1036px; height: 1200px; overflow: hidden; }
  body { background: var(--backdrop); position: relative; font-family: "Poppins", sans-serif; }

  .card {
    position: absolute;
    left: 109px;
    width: 823px;
    height: 470px;
    background: var(--yellow);
    overflow: hidden;
    box-shadow: 8px 10px 14px rgba(0,0,0,0.28);
  }
  .card--contact { top: 98px; }
  .card--brand { top: 625px; }

  .contact-band {
    position: absolute; left: 0; top: 0;
    width: 100%; height: 245px;
    background: var(--black);
  }
  .contact-line {
    position: absolute; left: 72px;
    display: flex; align-items: center;
    color: var(--white);
  }
  .contact-line--phone { top: 40px; }
  .contact-line--email { top: 128px; }
  .contact-icon { fill: var(--yellow); flex: none; }
  .phone-number {
    font-family: "Poppins", sans-serif;
    font-weight: 700;
    font-size: 84px;
    line-height: 1;
    letter-spacing: 1px;
    margin-left: 16px;
  }
  .email-address {
    font-family: "Poppins", sans-serif;
    font-weight: 500;
    font-size: 38.5px;
    line-height: 1;
    margin-left: 20px;
  }

  .service {
    position: absolute; top: 210px;
    width: 180px; margin-left: -90px;
    text-align: center;
  }
  .service--donate { left: 144px; }
  .service--recycle { left: 401px; }
  .service--dispose { left: 663px; }
  .service-badge {
    width: 92px; height: 92px; margin: 0 auto;
    border-radius: 50%;
    background: var(--black);
    border: 5px solid var(--white);
    display: flex; align-items: center; justify-content: center;
  }
  .service-badge svg { fill: var(--yellow); }
  .service-label {
    font-family: "Anton", sans-serif;
    font-size: 38px;
    line-height: 1;
    color: var(--black);
    letter-spacing: 1px;
    margin-top: 4px;
  }

  .web-address {
    position: absolute; left: 0; top: 390px;
    width: 100%;
    text-align: center;
    font-family: "Anton", sans-serif;
    font-size: 27px;
    line-height: 1;
    letter-spacing: 13.2px;
    text-indent: 13px;
    color: var(--black);
  }

  .brand-name {
    position: absolute; left: 0; top: 62px;
    width: 100%;
    text-align: center;
    font-family: "Anton", sans-serif;
    color: var(--black);
    line-height: 1;
  }
  .brand-name__main { display: block; font-size: 168px; letter-spacing: 4px; }
  .brand-name__sub { display: block; font-size: 70px; letter-spacing: 18px; text-indent: 18px; margin-top: 4px; }
</style>
</head>
<body>

  <section class="card card--contact">
    <div class="contact-band"></div>

    <div class="contact-line contact-line--phone">
      <svg class="contact-icon" width="52" height="52" viewBox="0 0 52 52" aria-hidden="true">
        <path d="M10 4 L18 4 L22 16 L16 21 C19 29 24 34 31 37 L36 31 L48 35 L48 43 C48 47 45 49 41 49 C22 47 6 31 4 12 C4 7 6 4 10 4 Z"/>
        <path d="M28 4 A20 20 0 0 1 48 24 L43 24 A15 15 0 0 0 28 9 Z"/>
        <path d="M28 13 A11 11 0 0 1 39 24 L34 24 A6 6 0 0 0 28 18 Z"/>
      </svg>
      <span class="phone-number">555-271-8093</span>
    </div>

    <div class="contact-line contact-line--email">
      <svg class="contact-icon" width="36" height="26" viewBox="0 0 36 26" aria-hidden="true">
        <path d="M0 0 H36 V26 H0 Z M3 3 V23 H33 V3 Z"/>
        <path d="M1 1 L18 15 L35 1 L35 4 L18 18 L1 4 Z"/>
        <path d="M1 24 L13 12 L15 14 L3 26 Z M35 24 L23 12 L21 14 L33 26 Z"/>
      </svg>
      <span class="email-address">info@harborhaulaway.example</span>
    </div>

    <div class="service service--donate">
      <div class="service-badge">
        <svg width="52" height="52" viewBox="0 0 52 52" aria-hidden="true">
          <path d="M27 28 C18 21 12 16 12 10 C12 5 16 2 20 2 C23 2 25 4 27 6 C29 4 31 2 34 2 C38 2 42 5 42 10 C42 16 36 21 27 28 Z"/>
          <rect x="2" y="31" width="7" height="17" rx="1.5"/>
          <path d="M12 32 H24 C27 32 28 34 27 36 H20 V39 H30 L41 31 C43 30 46 31 45 34 L34 46 C33 47 32 48 30 48 H12 Z"/>
        </svg>
      </div>
      <div class="service-label">DONATE</div>
    </div>

    <div class="service service--recycle">
      <div class="service-badge">
        <svg width="56" height="56" viewBox="0 0 56 56" aria-hidden="true">
          <path d="M21 6 H33 L40 18 L45 15 L41 29 L28 25 L33 22 L28 13 L21 25 L12 20 Z"/>
          <path d="M44 33 L50 44 L44 52 H31 V57 L22 46 L31 37 V43 H41 L36 35 Z"/>
          <path d="M6 44 L12 33 L7 30 L21 29 L24 42 L19 39 L14 48 H26 V52 H12 Z"/>
        </svg>
      </div>
      <div class="service-label">RECYCLE</div>
    </div>

    <div class="service service--dispose">
      <div class="service-badge">
        <svg width="56" height="56" viewBox="0 0 56 56" aria-hidden="true">
          <circle cx="43" cy="8" r="6"/>
          <path d="M35 17 H49 V50 L44 44 L40 50 H37 V32 L30 28 L32 24 L35 26 Z"/>
          <path d="M6 26 H30 L27 52 H9 Z M10 30 L12 48 H24 L26 30 Z"/>
          <path d="M18 34 L22 39 L18 44 L14 39 Z"/>
        </svg>
      </div>
      <div class="service-label">DISPOSE</div>
    </div>

    <p class="web-address">WWW.HARBORHAULAWAY.EXAMPLE</p>
  </section>

  <section class="card card--brand">
    <h1 class="brand-name">
      <span class="brand-name__main">HARBOR</span>
      <span class="brand-name__sub">HAUL AWAY</span>
    </h1>
    <p class="web-address">WWW.HARBORHAULAWAY.EXAMPLE</p>
  </section>

</body>
</html>
```